New design for weblog: joostvanleer.nl

My name is Joost van Leer, I am a tv presenter / radio-dj / writer from The Netherlands. I would like you to make a fresh new design for my weblog http://www.joostvanleer.nl. Please give it a 2010 look, with new colors and layout. Be creative, have fun!

Target Market(s)

- Fans and visitors of my blog
- Current and future employers

Number of Pages Required

1 page

Requirements
Must have
• - Must use my new "joostvanleer.nl" logo (as provided) 
Nice to have
• - Use the picture(s) i uploaded
Should not have
• x

```html
<!DOCTYPE html>
<html lang="nl">
<head>
<meta charset="utf-8">
<title>joostvanleer.nl – weblog</title>
<link href="https://fonts.googleapis.com/css2?family=Arimo:wght@400;700&family=Comfortaa:wght@400;700&display=swap" rel="stylesheet">
<style>
:root{
  --wood-light:#e8bf8f;
  --wood-dark:#d9a673;
  --blue:#29a9e1;
  --white:#ffffff;
  --text:#2f2f2f;
  --gold:#c9a13a;
  --yellow:#fccc4d;
  --tab-dark:#d9ad3c;
  --dots:#8c8c8c;
}
*{box-sizing:border-box;margin:0;padding:0}
html,body{width:1024px;height:1200px;overflow:hidden}
body{
  position:relative;
  font-family:"Arimo",Arial,sans-serif;
  color:var(--text);
  background:
    repeating-linear-gradient(90deg,rgba(255,255,255,.08) 0 2px,transparent 2px 9px,rgba(150,90,40,.06) 9px 11px,transparent 11px 23px),
    linear-gradient(90deg,var(--wood-light),var(--wood-dark) 50%,var(--wood-light));
}
.abs{position:absolute}
.frame{left:86px;top:164px;width:850px;height:962px;background:var(--blue)}
.sheet{left:101px;top:178px;width:819px;height:933px;background:var(--white)}

/* header visuals */
.papers{left:132px;top:36px;width:400px;height:430px;background:#f4f4f2;transform:rotate(-6deg);box-shadow:0 6px 14px rgba(0,0,0,.2)}
.papers.back{left:140px;top:42px;transform:rotate(-2deg);background:#fafafa}
.photo{left:262px;top:54px;width:262px;height:318px;background:#fff;padding:8px;transform:rotate(3deg);box-shadow:0 3px 8px rgba(0,0,0,.25)}
.photo .fill{width:100%;height:100%;background:linear-gradient(160deg,#8a8a88,#5a4a3e 55%,#6f7f99)}
.clock-area{left:117px;top:124px;width:108px;height:108px;background:linear-gradient(135deg,#d8d4d0,#b9b3ae)}
.pencil-area{left:690px;top:132px;width:245px;height:60px;background:linear-gradient(90deg,rgba(240,200,90,.35),rgba(240,200,90,.55))}
.bird-area{left:590px;top:376px;width:110px;height:108px;background:linear-gradient(180deg,#cfe9f6,#f7d3c4)}

.brand{left:574px;top:38px;display:flex;align-items:center;gap:10px}
.brand .mark{width:78px;height:78px;background:var(--blue);border-radius:12px}
.brand .name{font-size:34px;font-weight:700;color:var(--text);letter-spacing:-.5px}

/* tweet */
.tweets{left:570px;top:208px;width:332px;height:160px;border:3px solid var(--blue);border-radius:20px;background:var(--white);padding:21px 0 0 9px}
.tweet{margin-bottom:6px;font-size:11.2px;line-height:13px}
.tweet small{display:block;font-size:10px;line-height:12px}
.tail{left:690px;top:365px}
.tweet-label{left:708px;top:420px;font-family:"Comfortaa",sans-serif;font-size:25px;letter-spacing:1px;text-transform:uppercase;color:#3a3a3a}
.tweet-label span{color:var(--blue)}

/* posts */
.post{left:116px;width:426px}
.date{position:absolute;left:0;top:0;width:48px;height:46px;border-radius:4px;background:var(--yellow);text-align:center;color:#fff;box-shadow:0 1px 2px rgba(0,0,0,.2)}
.date .day{font-size:17px;line-height:26px}
.date .mon{background:var(--tab-dark);font-size:9px;line-height:14px;margin-top:4px;border-radius:0 0 4px 4px}
.post h2{position:absolute;left:56px;top:6px;font-size:16px;font-weight:700;color:#333}
.post .meta{position:absolute;left:56px;top:32px;font-size:9.6px}
.post p{position:absolute;left:0;top:59px;width:430px;font-size:11.4px;line-height:13.6px}
.post a{color:var(--gold);text-decoration:none}
.reacties{position:absolute;right:-2px;font-size:11px;font-weight:700;color:var(--gold)}
.rule{position:absolute;left:0;width:426px;border-top:1px dotted var(--dots)}
.video{position:absolute;left:40px;top:148px;width:353px;height:225px;background:linear-gradient(135deg,#111 0 40%,#4d5a66 40% 70%,#111 70%)}

/* sidebar lists */
.side h3{font-size:16px;font-weight:700;color:var(--gold);margin-bottom:11px;white-space:nowrap}
.side ul{list-style:none}
.side li{font-size:11.2px;line-height:19px;border-bottom:1px dotted var(--dots);margin-bottom:1px}
.archive{left:570px;top:510px;width:90px}
.people{left:702px;top:510px;width:140px}
.people ul{width:110px}

/* tabs */
.tabs{left:570px;top:820px;width:332px;height:248px;background:var(--yellow)}
.tabbar{display:flex;height:34px}
.tab{height:34px;line-height:34px;text-align:center;font-size:13px;font-weight:700;color:#fff;background:var(--tab-dark)}
.tab.active{background:var(--yellow);color:#3a3a3a;width:133px}
.tab.recent{width:106px;margin-right:2px}
.tab.articles{width:91px}
.tabs ul{list-style:none;padding:12px 14px 0 14px}
.tabs li{font-size:11.5px;height:30px;line-height:26px;border-bottom:1px dotted #8a7030}

.footer{left:0;top:1140px;width:1024px;text-align:center;font-size:10.4px;line-height:13px;color:#555}
</style>
</head>
<body>
<div class="abs frame"></div>
<div class="abs sheet"></div>

<div class="abs papers"></div>
<div class="abs papers back"></div>
<div class="abs photo"><div class="fill" role="img" aria-label="Foto van Joost in een rolstoel tussen kantoorgebouwen"></div></div>
<div class="abs clock-area" role="img" aria-label="Illustratie van een klok"></div>
<div class="abs pencil-area" role="img" aria-label="Illustratie van een geel potlood"></div>

<div class="abs brand"><span class="mark"></span><span class="name">joostvanleer.nl</span></div>

<div class="abs tweets">
  <div class="tweet"><b>John</b> : I’m the big fan of you! You’re extremely incredible!!!<small>about an hour ago</small></div>
  <div class="tweet"><b>John</b> : I’m the big fan of you! You’re extremely incredible!!!<small>about an hour ago</small></div>
  <div class="tweet"><b>John</b> : I’m the big fan of you! You’re extremely incredible!!!<small>about an hour ago</small></div>
  <div class="tweet"><b>John</b> : I’m the big fan of you! You’re extremely incredible!!!<small>about an hour ago</small></div>
</div>
<svg class="abs tail" width="40" height="30" viewBox="0 0 40 30"><path d="M2 0 L4 26 L30 2" fill="#fff" stroke="#29a9e1" stroke-width="3"/><rect x="3" y="0" width="26" height="3" fill="#fff"/></svg>
<div class="abs bird-area" role="img" aria-label="Illustratie van een vogeltje dat een boek leest"></div>
<div class="abs tweet-label">Latest <span>Tweet</span></div>

<article class="abs post" style="top:490px">
  <div class="date"><div class="day">31</div><div class="mon">NOV 09</div></div>
  <h2>Finales terugkijken?</h2>
  <div class="meta">Posted 10:32 am uur</div>
  <p>Afgelopen zondag was ik live te horen en zien vanaf centercourt bij het WK Rolstoeltennis, <a href="#">De Finaleweek in Amsterdam</a>. Daar ging de finale bij de mannen tussen Mick Schouten en Ruben Aalbers, gevolgd door de tevens compleet Nederlandse finale bij de dames Karin Hoeven - Elsa Verbeek. De wedstrijden waren integraal te volgen via Internet. Deze week zijn de wedstrijden nog in z’n geheel terug te kijken... <a href="#">(meer...)</a></p>
  <div class="reacties" style="top:147px">Reacties (9)</div>
  <div class="rule" style="top:164px"></div>
</article>

<article class="abs post" style="top:670px">
  <div class="date"><div class="day">31</div><div class="mon">NOV 09</div></div>
  <h2>Finales terugkijken?</h2>
  <div class="meta">Posted 10:32 am uur</div>
  <p>Afgelopen zondag was ik live te horen en zien vanaf centercourt bij het WK Rolstoeltennis, <a href="#">De Finaleweek in Amsterdam</a>. Daar ging de finale bij de mannen tussen Mick Schouten en Ruben Aalbers, gevolgd door de tevens compleet Nederlandse finale bij de dames Karin Hoeven - Elsa Verbeek. De wedstrijden waren integraal te volgen via Internet. Deze week zijn de wedstrijden nog in z’n geheel terug te kijken... <a href="#">(meer...)</a></p>
  <div class="video" role="img" aria-label="Videobeeld van de tennisbaan en de presentator in de studio"></div>
  <div class="reacties" style="top:388px">Reacties (9)</div>
  <div class="rule" style="top:408px"></div>
</article>

<nav class="abs side archive">
  <h3>Archief</h3>
  <ul>
    <li>January 2009</li><li>February 2009</li><li>March 2009</li><li>April 2009</li>
    <li>May 2009</li><li>June 2009</li><li>July 2009</li><li>August 2009</li>
    <li>September 2009</li><li>October 2009</li><li>November 2009</li><li style="border:0">December 2009</li>
  </ul>
</nav>
<nav class="abs side people">
  <h3>Leuke mensen</h3>
  <ul><li>Paps</li><li>Michel</li><li>Jeroen BVN</li><li>Manuel</li><li>Luuk</li><li>Youp</li></ul>
</nav>

<section class="abs tabs">
  <div class="tabbar">
    <div class="tab active">Most Popular</div>
    <div class="tab recent">Recent Post</div>
    <div class="tab articles">Articles</div>
  </div>
  <ul>
    <li><b>Duet</b> | 22-12-2009</li>
    <li><b>TV-kanaal</b> | 21-12-2009</li>
    <li><b>Stupid</b> | 15-12-2009</li>
    <li><b>Tennisfoto’s</b> | 06-12-2009</li>
    <li><b>Logokeus</b> | 06-12-2009</li>
    <li><b>Graanbank</b> | 05-12-2009</li>
  </ul>
</section>

<footer class="abs footer">©2002-2009 Joost van Leer<br>Alle rechten voorbehouden - <b>joost@joostvanleer.nl</b></footer>
</body>
</html>
```